Create Vertical Dog Food Labels (3 inches x 5 inches) for PupKitchen

We need a packing Vertical label (3 inches x 5 inches) design for our line of Dog Food - Pup Kitchen at pupkitchenmeals.com (please review website). This design is for Custom Roll Labels. We have a logo already. Use our logo colors on label. What we need incorporated is a list of our ingredients:

50% Choice Beef
20% Pasture-raised Chicken
15% Brown Rice
15% Fresh Vegetables - Carrots, Kale, Zucchini
Herbal Health Boosters

We also need these lines at the bottom of the label:

Keeps in fridge for 4 days after thawing
Stores in freezer up to 6 months
Questions? email us at orders@meadowlanepantry.com

We have attached a sample of a competitor. The Kibble Crate.

Target Market(s)

Dog owners

Industry/Entity Type

Dog Food

Font styles to use
Sans Serif

Requirements
Must have
• Read project description above
Nice to have
• Our logo color incorporated
Should not have
• I want it simple.

```html
<!DOCTYPE html>
<html lang="en">
<head>
<meta charset="UTF-8">
<title>PupKitchen Dog Food Label</title>
<link href="https://fonts.googleapis.com/css2?family=Ubuntu:wght@500;700&display=swap" rel="stylesheet">
<style>
  :root {
    --canvas-bg: #b3b3b3;
    --label-white: #ffffff;
    --pattern-grey: #ececec;
    --brand-green: #236b34;
    --brand-orange: #f5a31c;
    --warning-orange: #e9652a;
    --gold: #f2c14e;
    --ink: #1a1a1a;
  }
  * { margin: 0; padding: 0; box-sizing: border-box; }
  html, body {
    width: 1200px; height: 1200px; overflow: hidden;
    background: var(--canvas-bg);
    font-family: "Ubuntu", sans-serif;
  }
  .label {
    position: absolute; left: 280px; top: 84px;
    width: 640px; height: 1032px;
    background: var(--label-white);
    border-radius: 40px;
    overflow: hidden;
    display: flex; flex-direction: column;
  }
  .label__hero {
    position: relative;
    height: 516px;
    background: var(--pattern-grey);
  }
  .hero-art {
    position: absolute; inset: 0;
    background: radial-gradient(ellipse 62% 70% at 52% 52%, var(--brand-orange) 0%, var(--brand-orange) 45%, rgba(245,163,28,0.25) 62%, var(--pattern-grey) 78%);
  }
  .brand {
    position: absolute; left: 52px; top: 268px;
    display: flex; align-items: center; gap: 18px;
  }
  .brand__mark {
    width: 110px; height: 110px; border-radius: 50%;
    background: var(--label-white);
    border: 8px solid var(--brand-green);
  }
  .brand__name {
    font-weight: 700; font-size: 54px;
    color: var(--brand-green);
  }
  .rule { height: 5px; background: var(--brand-green); }
  .ingredients {
    height: 276px;
    display: flex; flex-direction: column; align-items: center;
    padding-top: 26px;
  }
  .ingredients__title {
    background: var(--brand-green); color: var(--label-white);
    font-weight: 700; font-size: 29px; letter-spacing: 1px;
    padding: 6px 22px; border-radius: 22px;
    margin-bottom: 20px;
  }
  .ingredients__list { list-style: none; text-align: center; }
  .ingredients__item {
    font-weight: 500; font-size: 21px; color: var(--ink);
    line-height: 37px;
    display: flex; align-items: center; justify-content: center; gap: 10px;
  }
  .ingredients__item::before {
    content: ""; width: 14px; height: 14px; border-radius: 50%;
    background: var(--ink);
  }
  .storage {
    height: 134px;
    background: var(--pattern-grey);
    display: flex; flex-direction: column; justify-content: center; align-items: center;
    gap: 10px;
  }
  .storage__line {
    font-weight: 700; font-size: 21px; color: var(--warning-orange);
    text-transform: uppercase;
  }
  .contact {
    flex: 1;
    background: var(--brand-green);
    display: flex; flex-direction: column; justify-content: center; align-items: center;
    gap: 6px;
  }
  .contact__prompt { font-weight: 700; font-size: 24px; color: var(--gold); }
  .contact__email { font-weight: 700; font-size: 21px; color: var(--label-white); }
</style>
</head>
<body>
  <main class="label">
    <section class="label__hero">
      <div class="hero-art" role="img" aria-label="Large orange paw print over a faint pet-themed doodle pattern"></div>
      <div class="brand">
        <span class="brand__mark"></span>
        <span class="brand__name">PupKitchen</span>
      </div>
    </section>
    <div class="rule"></div>
    <section class="ingredients">
      <h2 class="ingredients__title">INGREDIENTS:</h2>
      <ul class="ingredients__list">
        <li class="ingredients__item">50% Choice Beef</li>
        <li class="ingredients__item">20% Pasture-raised Chicken</li>
        <li class="ingredients__item">15% Brown Rice</li>
        <li class="ingredients__item">15% Fresh Vegetables - Carrots, Kale, Zucchini</li>
        <li class="ingredients__item">Herbal Health Boosters</li>
      </ul>
    </section>
    <div class="rule"></div>
    <section class="storage">
      <p class="storage__line">Keeps in fridge for 4 days after thawing</p>
      <p class="storage__line">Stores in freezer up to 6 months</p>
    </section>
    <footer class="contact">
      <p class="contact__prompt">Questions?</p>
      <p class="contact__email">email us at orders@meadowlanepantry.com</p>
    </footer>
  </main>
</body>
</html>
```